Create a banner for a Gmail email signature

We need a graphic design to use in a solicitor's email signature. The banner will incorporate a head shot of the solicitor as well as the law firm's logo and contact details. The solicitor's photo and law firm's logo are uploaded in the task.

```html
<!DOCTYPE html>
<html lang="en">
<head>
<meta charset="UTF-8">
<title>Email Signature – Maren Holloway</title>
<link href="https://fonts.googleapis.com/css2?family=Khand:wght@500&family=Poppins:wght@400;500&display=swap" rel="stylesheet">
<style>
  :root {
    --brand: #7d0a4a;
    --ink: #1b1b1b;
    --text: #333333;
    --paper: #ffffff;
    --rule: #c98aa8;
    --photo-top: #5f6f7e;
    --photo-mid: #c9b48a;
    --photo-low: #1f2633;
  }
  * { box-sizing: border-box; margin: 0; padding: 0; }
  html, body {
    width: 1200px;
    height: 722px;
    overflow: hidden;
    background: var(--paper);
    font-family: "Poppins", sans-serif;
  }
  .canvas { position: relative; width: 1200px; height: 722px; }

  .mockup-title {
    position: absolute;
    top: 58px;
    left: 0;
    width: 1156px;
    text-align: center;
    font-size: 29px;
    font-weight: 400;
    color: var(--brand);
    letter-spacing: 0.3px;
  }

  .signature {
    position: absolute;
    left: 150px;
    top: 156px;
    width: 900px;
    height: 452px;
    background: var(--paper);
    box-shadow: 0 2px 10px rgba(0,0,0,0.22);
  }

  .headshot {
    position: absolute;
    left: 31px;
    top: 33px;
    width: 288px;
    height: 288px;
    background: linear-gradient(160deg, var(--photo-top) 0%, #8f8c80 30%, var(--photo-mid) 55%, var(--photo-low) 100%);
  }

  .divider {
    position: absolute;
    left: 367px;
    top: 14px;
    width: 2px;
    height: 312px;
    background: var(--rule);
  }

  .person-name {
    position: absolute;
    left: 414px;
    top: 26px;
    font-family: "Khand", sans-serif;
    font-weight: 500;
    font-size: 48px;
    letter-spacing: 1px;
    color: var(--ink);
  }
  .person-role {
    position: absolute;
    left: 417px;
    top: 89px;
    font-size: 23px;
    color: var(--brand);
  }

  .contact-list {
    position: absolute;
    left: 417px;
    top: 150px;
    list-style: none;
  }
  .contact-item {
    display: flex;
    align-items: center;
    height: 42px;
    font-size: 21px;
    color: var(--text);
  }
  .contact-icon {
    width: 22px;
    height: 22px;
    margin-right: 24px;
    fill: var(--brand);
    flex: none;
  }

  .firm-mark {
    position: absolute;
    left: 30px;
    top: 362px;
    height: 66px;
    display: flex;
    align-items: center;
    gap: 12px;
  }
  .firm-dot {
    width: 22px;
    height: 22px;
    border-radius: 50%;
    background: var(--brand);
  }
  .firm-name {
    font-size: 31px;
    font-weight: 500;
    color: var(--brand);
    letter-spacing: 0.5px;
  }

  .social-band {
    position: absolute;
    left: 369px;
    top: 355px;
    width: 531px;
    height: 97px;
    background: var(--brand);
  }
  .social-label {
    position: absolute;
    left: 34px;
    top: 28px;
    font-size: 30px;
    font-weight: 500;
    color: var(--paper);
  }
  .social-links {
    position: absolute;
    left: 221px;
    top: 24px;
    display: flex;
    gap: 12px;
  }
  .social-link {
    width: 50px;
    height: 50px;
    border-radius: 50%;
    background: var(--paper);
  }
</style>
</head>
<body>
<div class="canvas">
  <h1 class="mockup-title">Email Signture-Design- Mockup 1</h1>

  <section class="signature">
    <div class="headshot" role="img" aria-label="Head shot of the solicitor"></div>
    <div class="divider"></div>

    <h2 class="person-name">Maren Holloway</h2>
    <p class="person-role">Solicitor</p>

    <ul class="contact-list">
      <li class="contact-item">
        <svg class="contact-icon" viewBox="0 0 24 24" aria-hidden="true"><path d="M6.6 10.8c1.4 2.8 3.8 5.1 6.6 6.6l2.2-2.2c.3-.3.7-.4 1-.2 1.1.4 2.3.6 3.6.6.6 0 1 .4 1 1V20c0 .6-.4 1-1 1C10.6 21 3 13.4 3 4c0-.6.4-1 1-1h3.5c.6 0 1 .4 1 1 0 1.3.2 2.5.6 3.6.1.3 0 .7-.2 1L6.6 10.8z"/></svg>
        555-014-2290
      </li>
      <li class="contact-item">
        <svg class="contact-icon" viewBox="0 0 24 24" aria-hidden="true"><path d="M8 2h8a2 2 0 0 1 2 2v16a2 2 0 0 1-2 2H8a2 2 0 0 1-2-2V4a2 2 0 0 1 2-2zm0 3v12h8V5H8zm4 13.2a1.1 1.1 0 1 0 0 2.2 1.1 1.1 0 0 0 0-2.2z"/></svg>
        555-018-7731
      </li>
      <li class="contact-item">
        <svg class="contact-icon" viewBox="0 0 24 24" aria-hidden="true"><path d="M3 5h18a1 1 0 0 1 1 1v1.2l-10 6-10-6V6a1 1 0 0 1 1-1zm-1 4.5 10 6 10-6V18a1 1 0 0 1-1 1H3a1 1 0 0 1-1-1V9.5z"/></svg>
        maren@quillpost.com
      </li>
      <li class="contact-item">
        <svg class="contact-icon" viewBox="0 0 24 24" aria-hidden="true"><path d="M12 2a10 10 0 1 0 0 20 10 10 0 0 0 0-20zm6.9 6h-2.9a15 15 0 0 0-1.4-3.9A8 8 0 0 1 18.9 8zM12 4c.8 1.1 1.5 2.5 1.9 4h-3.8c.4-1.5 1.1-2.9 1.9-4zM4.3 14a8 8 0 0 1 0-4h3.4a16 16 0 0 0 0 4H4.3zm.8 2h2.9c.3 1.4.8 2.7 1.4 3.9A8 8 0 0 1 5.1 16zM8 8H5.1a8 8 0 0 1 4.3-3.9C8.8 5.3 8.3 6.6 8 8zm4 12c-.8-1.1-1.5-2.5-1.9-4h3.8c-.4 1.5-1.1 2.9-1.9 4zm2.3-6H9.7a14 14 0 0 1 0-4h4.6a14 14 0 0 1 0 4zm.3 5.9c.6-1.2 1.1-2.5 1.4-3.9h2.9a8 8 0 0 1-4.3 3.9zm1.7-5.9a16 16 0 0 0 0-4h3.4a8 8 0 0 1 0 4h-3.4z"/></svg>
        marenholloway.com
      </li>
    </ul>

    <div class="firm-mark">
      <span class="firm-name">Harbourline Law</span>
      <span class="firm-dot"></span>
    </div>

    <div class="social-band">
      <p class="social-label">Follow Me</p>
      <div class="social-links">
        <span class="social-link" aria-label="Social profile 1"></span>
        <span class="social-link" aria-label="Social profile 2"></span>
        <span class="social-link" aria-label="Social profile 3"></span>
        <span class="social-link" aria-label="Social profile 4"></span>
      </div>
    </div>
  </section>
</div>
</body>
</html>
```